Yummy Mummy Flyer

Flyer that will be handed and also appear in magazine advertisements.

The campaign is aimed women that want to get pregnant, are pregnant or are post pregnancy. We are a private one-to-one pilates studio and will tailor packages to suit individual client's needs.

We want the colour scheme to be consistent to the website: www.delphinewarrickpilates.com We want the overall theme to exude exclusivity as our target market is the affluent upper middle class in Kensington and Chelsea, London
Updates

Hi Guys,

Thank you for the questions!
A5 please, one sided, landscape. 
All the best,
Delphine

To All the Designers,

Thank you so much for your submissions so far. I am extremely impressed with all of them! There are bits and pieces of a few designs that I think would look really nice if they were incorporated together. A few of
 the highlights are:
936979- I like this one, but please don't say, 'I am... (Delphine Warrick) please just put, 'Delphine with Talise 5 months'
934981- I really like the layout but not the color scheme on this one. Please put the web address as: www.delphinewarrickpilates.com
928472- This is my favorite design but the wording isn't quite right. 
927155-I like the layout and wording of this one.
931394- I like how, 'The Baby you dreamed of the body you deserve' is written. Please try and incorporate!
927947- I love how the website and studio logo is done. Please try and incorporate!
Thank you so much for all of your hard work and I look forward to seeing more of your submissions..
All the best,
Delphine

Reason: Hi! I am still waiting for the updated versions of the advert since my last comments... please email me if you have any questions... Thank you so much and looking forward to seeing the submissions soon... Delphine

Industry/Entity Type

Tailor

Requirements
Must have
• Incorporate the supplied photo (you can photoshop/alter the image as you see fit)

The picture is the studio owner with her daughter. Caption should read 'Delphine with daughter Talise, 5 months'

The design layout needs to work as both a flyer and as an advertisement in a magazine.

Needs to have website address, phone number (0207 611 3472), slogan 'The baby you dreamed of.....the body you deserve' & 'Whether you are pre or post pregnancy our team tailors programs for all stages'

You are free to suggest your take on how it looks, reads, design layout etc. Artistic freedom granted!
Nice to have
• Please refer to the attached recent press release by my PR agent. Please use any copy you feel necessary.

```html
<!DOCTYPE html>
<html lang="en">
<head>
<meta charset="utf-8">
<title>Delphine Warrick Private Pilates Studio – Flyer</title>
<link rel="stylesheet" href="https://fonts.googleapis.com/css2?family=Quicksand:wght@300;400&display=swap">
<style>
  :root {
    --pink: #c8196a;
    --purple: #52306f;
    --white: #ffffff;
    --soft-text: #f6e4ee;
    --caption-pink: #d0307a;
    --skin-light: #f1cdb2;
    --skin-mid: #e3ae8c;
    --swim-blue: #2f3f9c;
  }
  * { margin: 0; padding: 0; box-sizing: border-box; }
  html, body {
    width: 1200px;
    height: 846px;
    overflow: hidden;
    background: var(--white);
  }
  .flyer {
    position: relative;
    width: 1200px;
    height: 846px;
    overflow: hidden;
    font-family: "Quicksand", sans-serif;
  }
  .flyer__bands { position: absolute; inset: 0; }
  .band--pink { fill: var(--pink); }
  .band--purple { fill: var(--purple); }
  .photo-area { position: absolute; left: 750px; top: 0; }

  .studio-name {
    position: absolute;
    left: 30px;
    top: 30px;
    display: flex;
    align-items: center;
    gap: 16px;
    color: var(--white);
    font-weight: 400;
  }
  .studio-name__dot {
    width: 18px;
    height: 18px;
    border-radius: 50%;
    background: var(--white);
    flex: none;
  }
  .studio-name__title { font-size: 44px; line-height: 52px; font-weight: 400; }
  .studio-name__tagline { font-size: 22px; line-height: 30px; font-weight: 400; }

  .slogan {
    position: absolute;
    left: 30px;
    top: 178px;
    color: var(--soft-text);
    font-weight: 300;
    font-size: 36px;
    line-height: 48px;
    letter-spacing: 1px;
  }
  .slogan__first, .slogan__second { display: block; }
  .slogan__second { padding-left: 298px; }

  .copy {
    position: absolute;
    left: 30px;
    top: 308px;
    width: 520px;
    color: var(--soft-text);
    font-weight: 300;
    font-size: 22px;
    line-height: 36px;
    letter-spacing: 0.6px;
  }
  .copy p + p { margin-top: 18px; }
  .copy__stages { width: 400px; }

  .contact {
    position: absolute;
    left: 28px;
    top: 792px;
    color: var(--pink);
    font-weight: 300;
    font-size: 25px;
    letter-spacing: 0.8px;
    white-space: nowrap;
  }

  .photo-caption {
    position: absolute;
    left: 996px;
    top: 775px;
    color: var(--caption-pink);
    font-weight: 400;
    font-size: 16px;
    line-height: 22px;
  }
</style>
</head>
<body>
<main class="flyer">
  <svg class="flyer__bands" width="1200" height="846" viewBox="0 0 1200 846" aria-hidden="true">
    <polygon class="band--purple" points="0,0 1000,0 600,846 0,846"/>
    <polygon class="band--pink" points="0,0 880,0 0,520"/>
  </svg>

  <svg class="photo-area" width="380" height="760" viewBox="0 0 380 760" role="img" aria-label="Photo of the studio owner in a sun hat and blue bikini holding her baby daughter">
    <defs>
      <linearGradient id="photoTone" x1="0" y1="0" x2="0" y2="1">
        <stop offset="0" stop-color="var(--skin-light)"/>
        <stop offset="0.55" stop-color="var(--skin-mid)"/>
        <stop offset="0.72" stop-color="var(--swim-blue)"/>
        <stop offset="0.82" stop-color="var(--skin-mid)"/>
        <stop offset="1" stop-color="var(--skin-light)"/>
      </linearGradient>
    </defs>
    <rect x="0" y="0" width="380" height="760" rx="36" fill="url(#photoTone)"/>
  </svg>

  <header class="studio-name">
    <span class="studio-name__dot" aria-hidden="true"></span>
    <div>
      <h1 class="studio-name__title">Delphine Warrick</h1>
      <p class="studio-name__tagline">Private Pilates Studio</p>
    </div>
  </header>

  <h2 class="slogan">
    <span class="slogan__first">The baby you dreamed of...</span>
    <span class="slogan__second">...the body you deserve</span>
  </h2>

  <section class="copy">
    <p>Delphine Warrick’s studio offers one-to-one Pilates training for mum’s-to-be and can help mum’s spring back into shape afterwards.</p>
    <p>It also benefits your baby. Help your babies be more fit, smarter and easier to deal with by exercising throughout your pregnancy.</p>
    <p class="copy__stages">Whether you are pre or post pregnancy our team tailors programs for all stages.</p>
  </section>

  <p class="contact">Contact: 0207 611 3472 Online: www.delphinewarrickpilates.com</p>

  <p class="photo-caption">Delphine with daughter<br>Talise, 5 months</p>
</main>
</body>
</html>
```